I need a business card to launch my business. I am a carpenter who works with wood and metal framing. I do commercial and residential properties. I do the final fixtures in expensive residential properties. For example custom made wardrobes, prefinished doors and skirtings. I have an eye for detail and take pride in my work.

I don't want to be pigeon holed as a guy with a tool belt and a hammer. I want to look like a professional company. I want my logo to be modern and young and edgy. I don't have any preference for colours but don't want yellow.

Industry/Entity Type

Residential

Contact Information for Business Card

Cedar Line Carpentry
specialising in residential and commercial fit outs

Mark Dolan
Phone: 0413 528 036
cedarlinecarpentry@mailbrook.com

Logo styles of interest
Pictorial/Combination Logo
Wordmark Logo
Lettermark Logo

```html
<!DOCTYPE html>
<html lang="en">
<head>
<meta charset="utf-8">
<title>Cedar Line Carpentry – Business Card</title>
<link rel="stylesheet" href="https://fonts.googleapis.com/css2?family=Montserrat:wght@400;500;600;700&family=Lato:wght@700&family=EB+Garamond:wght@600&family=Tinos&display=swap">
<style>
  :root {
    --page: #ffffff;
    --ink: #1a1a1a;
    --card-dark: #1c1a19;
    --accent: #e2231a;
    --grey-mid: #868686;
    --grey-light: #aeaeae;
    --pattern: #f1f1f1;
    --white: #ffffff;
  }
  * { margin: 0; padding: 0; box-sizing: border-box; }
  html, body {
    width: 1200px; height: 694px; overflow: hidden;
    background: var(--page);
  }
  .sheet { position: relative; width: 1200px; height: 694px; }

  .side-label {
    position: absolute; top: 188px;
    font-family: "EB Garamond", serif; font-weight: 600; font-size: 20px;
    color: var(--ink);
  }
  .side-label--front { left: 175px; }
  .side-label--back { left: 662px; }

  .card {
    position: absolute; top: 225px; width: 455px; height: 257px;
    overflow: hidden;
  }
  .card--front { left: 145px; background: var(--white); border: 1px solid #cfcfcf; }
  .card--back { left: 616px; width: 453px; background: var(--card-dark); }

  .pattern-field {
    position: absolute; left: 0; right: 0; top: 19px; bottom: 19px;
    background: var(--pattern);
  }

  .band { position: absolute; left: 0; right: 0; height: 19px; display: flex; }
  .band--top { top: 0; }
  .band--bottom { bottom: 0; }
  .band span { display: block; height: 100%; }
  .band .black { background: var(--ink); flex: 1; }
  .band .mid { background: var(--grey-mid); width: 44px; }
  .band .light { background: var(--grey-light); width: 44px; }

  .brand {
    position: absolute; left: 45px; top: 96px;
    font-family: "Montserrat", sans-serif;
  }
  .brand-row { display: flex; align-items: center; gap: 6px; }
  .brand-mark { width: 36px; height: 36px; background: var(--accent); flex: none; }
  .brand-name {
    font-weight: 600; font-size: 15px; line-height: 18px;
    letter-spacing: 1px; color: var(--ink); text-transform: uppercase;
  }
  .brand-tagline {
    margin-top: 4px;
    font-weight: 700; font-size: 6.4px; color: var(--ink);
    white-space: nowrap;
  }

  .contact {
    position: absolute; left: 262px; width: 166px; top: 90px;
    text-align: center; color: var(--ink);
  }
  .contact-name {
    font-family: "Montserrat", sans-serif; font-weight: 500; font-size: 17px;
    line-height: 20px;
  }
  .contact-role {
    font-family: "Montserrat", sans-serif; font-weight: 500; font-size: 7.5px;
    letter-spacing: 3px; margin-top: 4px;
  }
  .contact-phone {
    font-family: "Montserrat", sans-serif; font-weight: 700; font-size: 12px;
    letter-spacing: 0.5px; margin-top: 3px;
  }
  .contact-email {
    font-family: "Tinos", serif; font-size: 7.2px; margin-top: 4px;
  }

  .back-brand {
    position: absolute; left: 0; right: 0; top: 78px;
    display: flex; flex-direction: column; align-items: center;
    font-family: "Montserrat", sans-serif;
  }
  .back-brand .brand-mark { width: 72px; height: 72px; }
  .back-brand .brand-name {
    color: var(--white); text-align: center; margin-top: 6px;
    font-size: 11px; line-height: 13px; letter-spacing: 1.6px;
  }

  .back-tagline {
    position: absolute; left: 0; right: 0; top: 234px;
    text-align: center; font-family: "Lato", sans-serif; font-weight: 700;
    font-size: 9.2px; letter-spacing: 2.6px; color: var(--white);
    white-space: nowrap;
  }
</style>
</head>
<body>
<main class="sheet">
  <p class="side-label side-label--front">front</p>
  <p class="side-label side-label--back">Back</p>

  <section class="card card--front" aria-label="Business card front">
    <div class="pattern-field" role="img" aria-label="Faint repeating brand pattern background"></div>
    <div class="band band--top"><span class="black"></span><span class="mid"></span><span class="light"></span></div>
    <div class="band band--bottom"><span class="light"></span><span class="mid"></span><span class="black"></span></div>

    <div class="brand">
      <div class="brand-row">
        <span class="brand-mark"></span>
        <p class="brand-name">Cedar Line<br>Carpentry</p>
      </div>
      <p class="brand-tagline">Specialising in Residential and Commercial Fit Outs</p>
    </div>

    <div class="contact">
      <p class="contact-name">Mark Dolan</p>
      <p class="contact-role">OWNER</p>
      <p class="contact-phone">0413-528-036</p>
      <p class="contact-email">cedarlinecarpentry@mailbrook.com</p>
    </div>
  </section>

  <section class="card card--back" aria-label="Business card back">
    <div class="back-brand">
      <span class="brand-mark"></span>
      <p class="brand-name">Cedar Line<br>Carpentry</p>
    </div>
    <p class="back-tagline">Specialising in Residential and Commercial Fit Outs</p>
  </section>
</main>
</body>
</html>
```